Corporate Two Sided Business Card

Looking for a Corporate "edgy" Modern look and feel for a business card

We are looking at two options. Dark background with our logo on it, white background with our logo on it - The background is more - Charcoal / Graphite then black

Details will be

Danielle Forsk

Licensee / Director

m. 0428 519 064

e. danielle@quorvela.com.au

quorvela.com.au

Target Market(s)

Professional Business people that refer use business and clients that own Investment Properties

Industry/Entity Type

Business

Contact Information for Business Card

Details will be

Danielle Forsk

Licensee / Director

m. 0428 519 064

quorvela.com.au

Font styles to use
Serif

Colors
000000
ec1f27
eeeeee
ffffff

Requirements
Must have
• Two options - White Background and Dark Background. - Two sided
Nice to have
• A design that is edgy, modern and new to look instead of boring style corporate cards - It should be a full integrated design
Should not have
• Block looking - Cheap.

```html
<!DOCTYPE html>
<html lang="en">
<head>
<meta charset="utf-8">
<title>Quorvela — Business Card</title>
<link rel="stylesheet" href="https://fonts.googleapis.com/css2?family=Montserrat:wght@500&family=Roboto:wght@300;500&display=swap">
<style>
  :root {
    --backdrop: #2a2a2a;
    --card: #1b1b1b;
    --card-edge: #111111;
    --text-soft: #a6a6a6;
    --text-muted: #8c8c8c;
    --accent: #ec1f27;
    --graphite: #5a5a5a;
  }
  * { margin: 0; padding: 0; box-sizing: border-box; }
  html, body { width: 1200px; height: 900px; overflow: hidden; }
  body {
    background: var(--backdrop);
    position: relative;
    font-family: "Roboto", Arial, sans-serif;
  }
  .card {
    position: absolute;
    top: 300px;
    width: 525px;
    height: 300px;
    background: var(--card);
    border: 1px solid var(--card-edge);
    box-shadow: 0 12px 30px rgba(0,0,0,0.45);
  }
  .card--front { left: 50px; }
  .card--back { left: 625px; display: flex; align-items: center; justify-content: center; }

  .brand {
    position: absolute;
    left: 40px;
    top: 52px;
    display: flex;
    align-items: center;
    gap: 10px;
  }
  .brand__mark { width: 16px; height: 16px; background: var(--accent); }
  .brand__name {
    font-family: "Montserrat", Arial, sans-serif;
    font-weight: 500;
    font-size: 38px;
    letter-spacing: 0.5px;
    color: var(--text-soft);
  }

  .contact {
    position: absolute;
    right: 38px;
    bottom: 46px;
    text-align: right;
    color: var(--text-muted);
    font-weight: 300;
    font-size: 13px;
    line-height: 1.45;
  }
  .contact__name {
    font-weight: 500;
    font-size: 16px;
    color: var(--text-soft);
    line-height: 1.2;
  }
  .contact__role { font-size: 10px; margin-bottom: 8px; }

  .back-brand { display: flex; align-items: center; gap: 12px; }
  .back-brand__mark { width: 22px; height: 22px; background: var(--graphite); }
  .back-brand__name {
    font-family: "Montserrat", Arial, sans-serif;
    font-weight: 500;
    font-size: 44px;
    color: var(--accent);
  }
</style>
</head>
<body>
  <section class="card card--front">
    <div class="brand">
      <span class="brand__mark"></span>
      <span class="brand__name">quorvela</span>
    </div>
    <div class="contact">
      <p class="contact__name">Danielle Forsk</p>
      <p class="contact__role">Licensee / Director</p>
      <p>0428 519 064</p>
      <p>danielle@quorvela.com.au</p>
      <p>www.quorvela.com.au</p>
    </div>
  </section>

  <section class="card card--back">
    <div class="back-brand">
      <span class="back-brand__name">quorvela</span>
      <span class="back-brand__mark"></span>
    </div>
  </section>
</body>
</html>
```